Marrup Wildtrail Quest 2017

We need a flyer designed for the Marrup Wildtrail Quest which is a multi sport event. It needs to have:
- the existing logo incorporated into the design
-Tarnby Harbour Society logo somewhere on the logo
- Wendale Shire logo
- website details: marrupwildtrailquest.net
- Enquiries: 0455 762 310
-Date: Saturday & Sunday October 14 & 15, 2017
-Saturday: Long Course, Sunday Short Course
- Team or Individual entries

I have attached some information and also an image of how I would like it to look around the logo with the photos I have supplied.

Thanks
Gareth

Target Market(s)

Athletes, local community, tourism

Industry/Entity Type

Tourism

Colors
0592cd
9ccb3b
f3f1f8

Requirements
Must have
• - the existing logo incorporated into the design
• -Tarnby Harbour Society logo somewhere on the logo
• - website details: marrupwildtrailquest.net
• - Enquiries: 0455 762 310
• -Date: Saturday & Sunday October 14 & 15, 2017
• -Saturday: Long Course, Sunday Short Course
• - Team or Individual entries
• I have attached some information and also an image of how I would like it to look around the logo with the photos I have supplied.
Nice to have
• Background trees and river

```html
<!DOCTYPE html>
<html lang="en">
<head>
<meta charset="utf-8">
<title>Marrup Wildtrail Quest 2017 – Flyer</title>
<link rel="stylesheet" href="https://fonts.googleapis.com/css2?family=Permanent+Marker&family=Raleway:wght@600;700;800&display=swap">
<style>
  :root {
    --blue: #0592cd;
    --lime: #c5d92a;
    --green: #9ccb3b;
    --paper: #f3f1f8;
    --ink: #111417;
    --night: #0d1012;
    --stage: #d6d6da;
    --white: #ffffff;
  }
  * { box-sizing: border-box; margin: 0; padding: 0; }
  html, body { width: 1200px; height: 1200px; overflow: hidden; }
  body {
    background: var(--stage);
    font-family: "Raleway", Arial, sans-serif;
    position: relative;
  }
  .flyer {
    position: absolute;
    left: 204px; top: 39px;
    width: 792px; height: 1122px;
    overflow: hidden;
  }
  .flyer__backdrop {
    position: absolute; inset: 0;
    background:
      radial-gradient(ellipse at 50% 20%, #6fd0f0 0%, transparent 55%),
      linear-gradient(180deg, #23a6d8 0%, #1a8fc4 35%, #2d6f6a 55%, #1b2a26 75%, var(--night) 100%);
  }
  .flyer__athletes {
    position: absolute;
    left: 68px; top: 226px; width: 656px; height: 360px;
    background: linear-gradient(180deg, rgba(240,220,200,.55) 0%, rgba(60,70,80,.7) 60%, rgba(30,120,170,.6) 100%);
    border-radius: 40px 40px 10px 10px;
  }
  .logo-badge {
    position: absolute;
    left: 292px; top: 22px; width: 208px; height: 208px;
    border-radius: 50%;
    background: var(--white);
    display: flex; align-items: center; justify-content: center;
    text-align: center;
    padding: 30px;
    font-weight: 800; font-size: 24px; line-height: 1.15;
    color: #4a3f38;
    text-transform: uppercase;
  }
  .date-tag {
    position: absolute;
    left: 612px; top: 2px; width: 152px; height: 156px;
    background: var(--ink);
    text-align: center;
    padding-top: 26px;
    font-weight: 800; line-height: 1.05;
    color: var(--white);
  }
  .date-tag__days { font-size: 29px; }
  .date-tag__month { font-size: 44px; color: var(--lime); }
  .date-tag__year { font-size: 20px; color: var(--lime); }
  .date-tag__weekend { font-size: 21px; margin-top: 4px; }
  .event-title {
    position: absolute;
    left: 0; top: 572px; width: 792px;
    text-align: center;
    font-family: "Permanent Marker", cursive;
    color: var(--white);
    font-size: 62px; line-height: 1.05;
    text-transform: uppercase;
  }
  .dates-band {
    position: absolute;
    left: 64px; top: 714px; width: 652px; height: 120px;
    background: var(--lime);
    clip-path: polygon(2% 4%, 100% 0, 98% 50%, 100% 100%, 0 96%, 3% 50%);
    text-align: center;
    color: var(--ink);
    padding-top: 22px;
    font-weight: 800;
  }
  .dates-band__days { font-size: 38px; line-height: 1.1; }
  .dates-band__full { font-size: 29px; line-height: 1.2; }
  .courses-band {
    position: absolute;
    left: 12px; top: 838px; width: 772px; height: 68px;
    background: var(--blue);
    clip-path: polygon(1% 10%, 100% 0, 99% 55%, 100% 100%, 0 92%, 2% 50%);
    color: var(--paper);
    font-weight: 700; font-size: 20px; line-height: 1.1;
    display: flex; align-items: center;
  }
  .courses-band__left { width: 408px; text-align: right; padding-right: 14px; }
  .courses-band__divider { width: 3px; height: 60px; background: var(--white); }
  .courses-band__right { padding-left: 24px; }
  .partner-strip {
    position: absolute;
    left: 224px; top: 911px; width: 344px; height: 78px;
    background: var(--white);
    display: flex; align-items: center; justify-content: space-around;
    padding: 0 8px;
    font-weight: 700; font-size: 13px; line-height: 1.15;
    color: #2a4a8a;
  }
  .partner { display: flex; align-items: center; gap: 6px; }
  .partner__dot { width: 22px; height: 22px; border-radius: 50%; background: var(--blue); flex: none; }
  .partner__square { width: 22px; height: 22px; background: #3b5a9a; flex: none; }
  .contact {
    position: absolute;
    left: 0; width: 792px; text-align: center; color: var(--white); font-weight: 700;
  }
  .contact__label { top: 1002px; font-size: 18px; }
  .contact__web { top: 1024px; font-size: 31px; text-transform: uppercase; }
  .contact__phone { top: 1064px; font-size: 30px; }
</style>
</head>
<body>
  <article class="flyer">
    <div class="flyer__backdrop" role="img" aria-label="Sky, bush trees and river scenery"></div>
    <div class="flyer__athletes" role="img" aria-label="Athletes cycling, running, swimming and kayaking"></div>

    <div class="logo-badge">Marrup Wildtrail Quest</div>

    <div class="date-tag">
      <div class="date-tag__days">14 &amp; 15</div>
      <div class="date-tag__month">OCT</div>
      <div class="date-tag__year">2017</div>
      <div class="date-tag__weekend">SAT &amp; SUN</div>
    </div>

    <h1 class="event-title">Marrup Wildtrail<br>Quest 2017</h1>

    <div class="dates-band">
      <div class="dates-band__days">SATURDAY &amp; SUNDAY</div>
      <div class="dates-band__full">OCTOBER 14 &amp; 15, 2017</div>
    </div>

    <div class="courses-band">
      <div class="courses-band__left">SATURDAY: LONG COURSE<br>SUNDAY SHORT COURSE</div>
      <div class="courses-band__divider"></div>
      <div class="courses-band__right">TEAM OR INDIVIDUAL<br>ENTRIES</div>
    </div>

    <div class="partner-strip">
      <div class="partner"><span class="partner__square"></span>Trailtalk</div>
      <div class="partner"><span class="partner__dot"></span>Wendale<br>Shire</div>
      <div class="partner">Tarnby Harbour<br>Society</div>
    </div>

    <p class="contact contact__label">Contact us</p>
    <p class="contact contact__web">www.marrupwildtrailquest.net</p>
    <p class="contact contact__phone">0455 762 310</p>
  </article>
</body>
</html>
```